COVID-19 Related Signage for Hotel

Need to create new COVID-19 related signage utilizing our brand assets. Please use screenshots for copy/direction. essentially duplicate the screenshots but with our logo/branding.

All brand assets have been uploaded and examples of signage content. Pictures are not necessary but you can add them if you want similar to the examples attached.

Sign requirements

sign 1. Text "Hand Sanitizer Station" can add graphic
sign 2. Text "Protect Yourself" duplicate copy in the attached pictures
sign 3. Text "Face Mask Required" can add graphic
sign 4. Text "Face Covering Do's and Don'ts with text from "Face-covering checklist.jpg" REMOVE BWT logo or website or 3 face mask graphics
sign 5. Text "Maintain 6 Foot Distance" This sign will be printed and placed on the ground for guests to know where to stand in queue. Would prefer a circular Design. sign 6. Text "Wet, Lather, Scrub, Rinse, Dry" similar to screenshots attached.

ALL signs should have same look and feel throughout utilizing our brand graphics, logo, colors, and guidelines.

Target Market(s)

Hotel Guests

Industry/Entity Type

Hotel

Font styles to use
Sans Serif

Requirements
Must have
• Cohesive, unified branding look and feel

Should not have
• any use of the word "COVID-19" or Coronavirus.

```html
<!DOCTYPE html>
<html lang="en">
<head>
<meta charset="utf-8">
<title>Face Covering Do's &amp; Don'ts</title>
<link href="https://fonts.googleapis.com/css2?family=Oswald:wght@300;400&display=swap" rel="stylesheet">
<style>
  :root {
    --brand-orange: #f47b20;
    --paper: #ffffff;
    --pattern-grey: #ececec;
  }
  * { margin: 0; padding: 0; box-sizing: border-box; }
  html, body { width: 848px; height: 1200px; overflow: hidden; background: var(--paper); }
  .sign {
    position: relative;
    width: 848px;
    height: 1200px;
    background: var(--paper);
    font-family: "Oswald", "Arial Narrow", sans-serif;
    font-weight: 300;
    color: var(--brand-orange);
  }
  .header-band {
    position: absolute; left: 0; top: 0;
    width: 848px; height: 126px;
    background: var(--pattern-grey);
  }
  .footer-band {
    position: absolute; left: 0; top: 1143px;
    width: 848px; height: 57px;
    background: var(--brand-orange);
  }
  .brand {
    position: absolute; left: 0; top: 156px;
    width: 848px;
    display: flex; align-items: center; justify-content: center;
    gap: 12px;
  }
  .brand-dot {
    width: 14px; height: 14px;
    border-radius: 50%;
    background: var(--brand-orange);
  }
  .brand-name {
    font-weight: 300;
    font-size: 26px;
    letter-spacing: 3px;
    line-height: 1;
    white-space: nowrap;
  }
  .title {
    position: absolute; left: 118px; top: 278px;
    font-size: 47px; font-weight: 400;
    letter-spacing: 2.7px;
    line-height: 1;
    white-space: nowrap;
  }
  .title-rule {
    position: absolute; left: 118px; top: 347px;
    width: 614px; height: 5px;
    background: var(--brand-orange);
  }
  .list-heading {
    position: absolute; left: 118px;
    font-size: 33px; font-weight: 400;
    letter-spacing: 3px; line-height: 1;
  }
  .list-heading.do { top: 422px; }
  .list-heading.dont { top: 791px; }
  .item {
    position: absolute; left: 92px;
    display: flex; align-items: center;
    height: 40px;
    font-size: 33px; letter-spacing: 3.85px;
    white-space: nowrap;
  }
  .item svg { width: 38px; height: 38px; margin-right: 16px; flex: none; }
  .continuation {
    position: absolute; left: 141px; top: 979px;
    font-size: 33px; letter-spacing: 3.6px; line-height: 40px;
    white-space: nowrap;
  }
</style>
</head>
<body>
<main class="sign">
  <div class="header-band" role="img" aria-label="Light grey decorative swirl pattern band"></div>

  <div class="brand">
    <span class="brand-dot"></span>
    <span class="brand-name">Cedar Basin Lodge</span>
  </div>

  <h1 class="title">FACE COVERING DO’S &amp; DON’TS:</h1>
  <div class="title-rule"></div>

  <h2 class="list-heading do">DO:</h2>
  <div class="item" style="top:482px">
    <svg viewBox="0 0 38 38"><circle cx="19" cy="19" r="19" fill="#f47b20"/><path d="M10 19.5l6 6 12-12" fill="none" stroke="#fff" stroke-width="4" stroke-linecap="round" stroke-linejoin="round"/></svg>
    Make sure you can breathe through it
  </div>
  <div class="item" style="top:545px">
    <svg viewBox="0 0 38 38"><circle cx="19" cy="19" r="19" fill="#f47b20"/><path d="M10 19.5l6 6 12-12" fill="none" stroke="#fff" stroke-width="4" stroke-linecap="round" stroke-linejoin="round"/></svg>
    Wear it whenever doing out in public
  </div>
  <div class="item" style="top:609px">
    <svg viewBox="0 0 38 38"><circle cx="19" cy="19" r="19" fill="#f47b20"/><path d="M10 19.5l6 6 12-12" fill="none" stroke="#fff" stroke-width="4" stroke-linecap="round" stroke-linejoin="round"/></svg>
    Make sure it covers your nose &amp; mouth
  </div>
  <div class="item" style="top:672px">
    <svg viewBox="0 0 38 38"><circle cx="19" cy="19" r="19" fill="#f47b20"/><path d="M10 19.5l6 6 12-12" fill="none" stroke="#fff" stroke-width="4" stroke-linecap="round" stroke-linejoin="round"/></svg>
    Wash after using
  </div>

  <h2 class="list-heading dont">DON’T:</h2>
  <div class="item" style="top:852px">
    <svg viewBox="0 0 38 38"><circle cx="19" cy="19" r="19" fill="#f47b20"/><path d="M13 13l12 12M25 13l-12 12" stroke="#fff" stroke-width="4" stroke-linecap="round"/></svg>
    Use if under two years old
  </div>
  <div class="item" style="top:915px">
    <svg viewBox="0 0 38 38"><circle cx="19" cy="19" r="19" fill="#f47b20"/><path d="M13 13l12 12M25 13l-12 12" stroke="#fff" stroke-width="4" stroke-linecap="round"/></svg>
    Use surgical masks or other PPE intended
  </div>
  <div class="continuation">for healthcare workers</div>

  <div class="footer-band" role="img" aria-label="Orange decorative swirl pattern band"></div>
</main>
</body>
</html>
```